bluefernworks.com website design

We're looking for a website design for Bluefernworks.com .
Bluefern is a manufacturer of high visibility traffic safety equipment and gear.. Our initial site will be a product catalog site featuring traffic cones . We will eventually expand to include traffic barriers, mesh signs, safety clothing and more. Our logo and product pictures can be found at bluefernworks.com .
Updates

Target Market(s)

We service a wide range of customers with our focus markets being construction, manufacturing and municipalities.

Industry/Entity Type

Safety Products

Number of Pages Required

1 page

Font styles to use
Sans Serif

Requirements
Must have
• company logo w/compatible color scheme

```html
<!DOCTYPE html>
<html lang="en">
<head>
<meta charset="utf-8">
<title>Bluefern Safety Products</title>
<link href="https://fonts.googleapis.com/css2?family=Roboto:wght@400;500;700&display=swap" rel="stylesheet">
<style>
:root{
  --orange:#e8913f;
  --orange-deep:#e3862f;
  --green:#7cbc5f;
  --ink:#222;
  --muted:#555;
  --line:#e3e3e3;
  --dark:#2a2b2d;
  --white:#fff;
}
*{margin:0;padding:0;box-sizing:border-box}
html,body{width:1200px;height:3785px;overflow:hidden}
body{position:relative;font-family:'Roboto',sans-serif;color:var(--ink);background:var(--white)}
a{color:inherit;text-decoration:none}
.abs{position:absolute}

/* header */
.site-header{position:absolute;left:0;top:0;width:1200px;height:110px;background:var(--white);z-index:5}
.catalog-pill{left:150px;top:18px;width:188px;height:32px;border-radius:16px;background:var(--green);color:#fff;font-size:12px;font-weight:500;display:flex;align-items:center;justify-content:center;letter-spacing:.2px}
.header-mail{right:150px;top:18px;display:flex;align-items:center;gap:10px;font-size:12px}
.mail-dot{width:28px;height:28px;border-radius:50%;background:var(--orange);display:flex;align-items:center;justify-content:center}
.brand{left:0;width:1200px;top:38px;text-align:center;font-size:36px;font-weight:700;color:var(--orange)}
.nav a{position:absolute;top:72px;font-size:16px;color:#444}
.nav a.active{color:var(--orange);font-weight:500}

/* hero */
.hero{left:0;top:110px;width:1200px;height:680px;overflow:hidden}
.hero-photo{position:absolute;inset:0;background:
  radial-gradient(ellipse 90px 260px at 310px 470px,rgba(240,100,40,.85),transparent 70%),
  radial-gradient(ellipse 70px 220px at 640px 330px,rgba(240,100,40,.8),transparent 70%),
  radial-gradient(ellipse 50px 170px at 800px 300px,rgba(240,100,40,.75),transparent 70%),
  radial-gradient(ellipse 40px 140px at 975px 260px,rgba(240,100,40,.75),transparent 70%),
  radial-gradient(ellipse 110px 70px at 1010px 230px,rgba(225,225,225,.55),transparent 70%),
  linear-gradient(180deg,#5b5a4f 0%,#5e5a52 30%,#45433f 60%,#333334 100%)}
.hero-curve{position:absolute;left:0;top:0}
.hero h1{position:absolute;left:0;width:1200px;top:210px;text-align:center;color:#fff;font-size:64px;font-weight:700;line-height:76px}
.btn{display:flex;align-items:center;justify-content:center;background:var(--green);color:#fff;font-weight:500;border-radius:28px}
.hero .btn{position:absolute;left:499px;top:390px;width:202px;height:53px;font-size:20px}

/* section headings */
.section-title{left:0;width:1200px;text-align:center;color:var(--orange);font-size:56px;font-weight:700}
.section-lede{left:0;width:1200px;text-align:center;font-size:13px;line-height:20px;color:#333}

/* products */
.product{width:212px;height:290px;background:#fff;border:1px solid var(--line);box-shadow:0 2px 6px rgba(0,0,0,.12)}
.product .shot{height:178px;border-bottom:1px solid var(--line);display:flex;align-items:center;justify-content:center}
.product .shot span{display:block}
.product h3{margin-top:22px;text-align:center;color:var(--orange);font-size:19px;font-weight:500}
.product p{margin:12px 24px 0;text-align:center;font-size:11px;line-height:16px;color:#444}

/* about */
.about{left:0;top:1846px;width:1200px;height:468px;background:
  radial-gradient(ellipse 60px 180px at 1100px 260px,rgba(240,110,40,.45),transparent 70%),
  radial-gradient(ellipse 50px 150px at 960px 330px,rgba(240,110,40,.4),transparent 70%),
  linear-gradient(120deg,#e28a3c 0%,#e9944a 50%,#dc8a45 100%)}
.about-mark{position:absolute;left:170px;top:170px;display:flex;align-items:center;gap:18px;color:#fff;font-size:52px;font-weight:700}
.about-mark i{display:block;width:70px;height:70px;border-radius:50%;background:#fff}
.about h2{position:absolute;left:558px;top:80px;color:#fff;font-size:54px;font-weight:700}
.about p{position:absolute;left:558px;top:174px;width:500px;color:#fff;font-size:13px;line-height:17.6px}
.about .btn{position:absolute;left:557px;top:338px;width:270px;height:49px;font-size:18px;border:2px solid #fff}

/* blog */
.blog-photo{width:284px;height:203px}
.blog-card{width:253px;height:198px;background:#fff;border-radius:10px;box-shadow:0 3px 10px rgba(0,0,0,.15);padding:20px 20px 0}
.blog-date{display:flex;align-items:center;gap:10px;font-size:13px}
.blog-card h4{margin-top:12px;font-size:12.5px;line-height:18px;font-weight:700}
.blog-card p{margin-top:8px;font-size:11px;line-height:15px;color:#444}
.blog-card .more{display:block;margin-top:10px;color:var(--orange);font-size:13px;font-weight:700}

/* contact */
.contact{left:0;top:3030px;width:1200px;height:755px;overflow:hidden}
.contact-photo{position:absolute;inset:0;background:
  radial-gradient(ellipse 200px 160px at 150px 400px,rgba(120,110,70,.35),transparent 70%),
  radial-gradient(ellipse 40px 70px at 140px 520px,rgba(220,90,40,.35),transparent 70%),
  linear-gradient(180deg,#3a3a3a 0%,#2b2c2d 45%,#232425 100%)}
.contact-curve{position:absolute;left:0;top:0}
.contact h2{position:absolute;left:0;width:1200px;top:140px;text-align:center;color:var(--orange);font-size:56px;font-weight:700}
.field{position:absolute;border:1.5px solid #eee;color:#fff;font-size:13px;padding:10px 14px}
.contact .btn{position:absolute;left:538px;top:465px;width:124px;height:50px;font-size:19px;border:2px solid #fff}
.rule{position:absolute;left:0;width:1200px;top:550px;height:1px;background:rgba(255,255,255,.25)}
.footer-nav{position:absolute;left:0;width:1200px;top:598px;text-align:center;color:#fff;font-size:16px}
.footer-nav a{margin:0 20px}
.copyright{position:absolute;left:0;width:1200px;top:648px;text-align:center;color:#fff;font-size:12px}
.footer-mail{position:absolute;left:0;width:1200px;top:678px;display:flex;justify-content:center;align-items:center;gap:10px;color:#fff;font-size:15px}
</style>
</head>
<body>

<header class="site-header">
  <a class="abs catalog-pill" href="#">DOWNLOAD PRODUCT CATALOG</a>
  <div class="abs header-mail">
    <span class="mail-dot"><svg width="14" height="10" viewBox="0 0 14 10"><rect x="0.5" y="0.5" width="13" height="9" rx="1" fill="none" stroke="#fff"/><path d="M1 1l6 5 6-5" fill="none" stroke="#fff"/></svg></span>
    info@bluefernworks.com
  </div>
  <div class="abs brand">Bluefern</div>
  <nav class="nav">
    <a class="active" href="#" style="left:148px">Home</a>
    <a href="#" style="left:224px">About Us</a>
    <a href="#" style="left:322px">Services</a>
    <a href="#" style="left:842px">Traffic Cones</a>
    <a href="#" style="left:970px">Contact Us</a>
  </nav>
</header>

<section class="abs hero">
  <div class="hero-photo" role="img" aria-label="Photo of orange traffic cones lined along a street"></div>
  <svg class="hero-curve" width="1200" height="680" viewBox="0 0 1200 680">
    <path d="M0 520 C300 690 850 680 1200 480 L1200 680 L0 680Z" fill="#fff"/>
    <path d="M0 530 C300 700 850 690 1200 492" fill="none" stroke="#e8913f" stroke-width="12"/>
  </svg>
  <h1>Always Getting You<br>Home Safely</h1>
  <a class="btn" href="#">GET IN TOUCH</a>
</section>

<h2 class="abs section-title" style="top:888px">Our Products</h2>
<p class="abs section-lede" style="top:972px">Lorem ipsum dolor sit amet, consectetur adipiscing elit, sed do eiusmod tempor incididunt ut labore et dolore magna aliqua.<br>Ut enim ad minim veniam, quis nostrud exercitation ullamco laboris nisi ut aliquip ex ea commodo consequat.</p>

<div class="abs product" style="left:148px;top:1055px"><div class="shot"><span role="img" aria-label="Orange traffic cone with white reflective bands" style="width:60px;height:142px;background:radial-gradient(ellipse 40px 60px at 50% 60%,#f47a2a,#ffd9c2 130%)"></span></div><h3>Traffic Cones</h3><p>Lorem ipsum dolor sit amet, co tetur ado e et dolo aliqua.</p></div>
<div class="abs product" style="left:378px;top:1055px"><div class="shot"><span role="img" aria-label="Orange and white striped traffic barrier" style="width:120px;height:120px;background:radial-gradient(ellipse 60px 45px at 50% 50%,#ee9448,#f3f3f3 120%)"></span></div><h3>Traffic Barriers</h3><p>Lorem ipsum dolor sit amet, co tetur ado e et dolo aliqua.</p></div>
<div class="abs product" style="left:607px;top:1055px"><div class="shot"><span role="img" aria-label="Grey mesh sign panel on two posts" style="width:136px;height:90px;background:radial-gradient(ellipse 70px 45px at 50% 50%,#efefef,#b4b4b4 140%)"></span></div><h3>Mesh Sign</h3><p>Lorem ipsum dolor sit amet, co tetur ado e et dolo aliqua.</p></div>
<div class="abs product" style="left:837px;top:1055px"><div class="shot"><span role="img" aria-label="Orange and yellow high visibility safety vests" style="width:140px;height:148px;background:linear-gradient(180deg,#f39a3c 0%,#f0a050 48%,#d9ea44 52%,#c9e23a 100%)"></span></div><h3>Safety Clothing</h3><p>Lorem ipsum dolor sit amet, co tetur ado e et dolo aliqua.</p></div>

<div class="abs product" style="left:148px;top:1368px"><div class="shot"><span role="img" aria-label="Orange hard hat" style="width:124px;height:100px;background:radial-gradient(ellipse 62px 50px at 50% 55%,#f7a33a,#fde3c6 130%)"></span></div><h3>Safety Hat</h3><p>Lorem ipsum dolor sit amet, co tetur ado e et dolo aliqua.</p></div>
<div class="abs product" style="left:378px;top:1368px"><div class="shot"><span role="img" aria-label="Clear safety glasses with black frame" style="width:180px;height:72px;background:radial-gradient(ellipse 90px 36px at 50% 50%,#f4f4f4,#8a8a8a 150%)"></span></div><h3>Safety Specs</h3><p>Lorem ipsum dolor sit amet, co tetur ado e et dolo aliqua.</p></div>
<div class="abs product" style="left:607px;top:1368px"><div class="shot"><span role="img" aria-label="Pair of orange work gloves" style="width:100px;height:130px;background:radial-gradient(ellipse 50px 65px at 50% 50%,#f0a040,#fbe4c4 130%)"></span></div><h3>Safety Gloves</h3><p>Lorem ipsum dolor sit amet, co tetur ado e et dolo aliqua.</p></div>
<div class="abs product" style="left:837px;top:1368px"><div class="shot"><span role="img" aria-label="Lime green traffic cone with white bands" style="width:60px;height:146px;background:radial-gradient(ellipse 40px 60px at 50% 60%,#8fe03a,#e4f8cc 130%)"></span></div><h3>Traffic Cones</h3><p>Lorem ipsum dolor sit amet, co tetur ado e et dolo aliqua.</p></div>

<a class="abs btn" href="#" style="left:480px;top:1695px;width:240px;height:49px;font-size:18px">DOWNLOAD CATALOG</a>

<section class="abs about" role="img" aria-label="Orange tinted photo of a road work zone with cones">
  <div class="about-mark"><i></i>Bluefern</div>
  <h2>About Bluefern</h2>
  <p>Lorem ipsum dolor sit amet, consectetur adipiscing elit, sed do eiusmod tempor incididunt ut labore et dolore magna aliqua. Ut enim ad minim veniam, quis nostrud exercitation ullamco laboris nisi ut aliquip ex ea commodo consequat. Duis aute irure dolor in reprehenderit in voluptate velit esse cillum dolore eu fugiat nulla pariatur. Excepteur sint occaecat cupidatat non proident, sunt in culpa qui officia deserunt mollit anim id est laborum.Sed ut perspiciatis unde omnis iste natus error sit voluptatem accusantium doloremque laudantium, totam rem aperiam, eaque ipsa quae atecto beatae vitae dicta sunt explicabo.</p>
  <a class="btn" href="#">LEARN MORE ABOUT US</a>
</section>

<h2 class="abs section-title" style="top:2412px">Latest Blog</h2>
<p class="abs section-lede" style="top:2496px">Lorem ipsum dolor sit amet, consectetur adipiscing elit, sed do eiusmod tempor incididunt ut labore et dolore magna aliqua.<br>Ut enim ad minim veniam, quis nostrud exercitation ullamco laboris nisi ut aliquip ex ea commodo consequat.</p>

<div class="abs blog-photo" role="img" aria-label="Road work trailer with cones and barriers" style="left:150px;top:2580px;background:radial-gradient(ellipse 90px 60px at 45% 70%,rgba(235,140,50,.9),transparent 75%),linear-gradient(180deg,#4c5a44 0%,#6a6a58 45%,#b48a4a 100%)"></div>
<div class="abs blog-photo" role="img" aria-label="No entry sign in front of a fenced site" style="left:459px;top:2580px;background:radial-gradient(circle 28px at 32% 52%,#d2332b 60%,transparent 64%),linear-gradient(180deg,#c8c4bb 0%,#9d978a 50%,#6f6a60 100%)"></div>
<div class="abs blog-photo" role="img" aria-label="Work boots, hard hat and ear protection" style="left:766px;top:2580px;background:radial-gradient(ellipse 50px 45px at 82% 40%,#f3c52c,transparent 75%),radial-gradient(ellipse 60px 40px at 25% 45%,#5c4a3a,transparent 80%),linear-gradient(180deg,#c9552b 0%,#b8673f 45%,#8c8478 100%)"></div>

<article class="abs blog-card" style="left:165px;top:2745px">
  <div class="blog-date"><svg width="26" height="26" viewBox="0 0 26 26"><rect x="1" y="4" width="24" height="21" rx="2" fill="#7cbc5f"/><rect x="6" y="1" width="3" height="6" fill="#7cbc5f"/><rect x="17" y="1" width="3" height="6" fill="#7cbc5f"/><g fill="#fff"><rect x="5" y="11" width="4" height="3"/><rect x="11" y="11" width="4" height="3"/><rect x="17" y="11" width="4" height="3"/><rect x="5" y="17" width="4" height="3"/><rect x="11" y="17" width="4" height="3"/><rect x="17" y="17" width="4" height="3"/></g></svg>February 04,2023</div>
  <h4>Lorem ipsum dolor sit amet, conse ctetur magna dolor aliqua.</h4>
  <p>Lorem ipsum dolor sit amet, consectetur adipiscing elit, sed do eiusmod tempor incididunt ut labore et &nbsp;magna aliqua.</p>
  <a class="more" href="#">READ MORE</a>
</article>
<article class="abs blog-card" style="left:474px;top:2745px">
  <div class="blog-date"><svg width="26" height="26" viewBox="0 0 26 26"><rect x="1" y="4" width="24" height="21" rx="2" fill="#7cbc5f"/><rect x="6" y="1" width="3" height="6" fill="#7cbc5f"/><rect x="17" y="1" width="3" height="6" fill="#7cbc5f"/><g fill="#fff"><rect x="5" y="11" width="4" height="3"/><rect x="11" y="11" width="4" height="3"/><rect x="17" y="11" width="4" height="3"/><rect x="5" y="17" width="4" height="3"/><rect x="11" y="17" width="4" height="3"/><rect x="17" y="17" width="4" height="3"/></g></svg>February 04,2023</div>
  <h4>Lorem ipsum dolor sit amet, conse ctetur magna dolor aliqua.</h4>
  <p>Lorem ipsum dolor sit amet, consectetur adipiscing elit, sed do eiusmod tempor incididunt ut labore et &nbsp;magna aliqua.</p>
  <a class="more" href="#">READ MORE</a>
</article>
<article class="abs blog-card" style="left:781px;top:2745px">
  <div class="blog-date"><svg width="26" height="26" viewBox="0 0 26 26"><rect x="1" y="4" width="24" height="21" rx="2" fill="#7cbc5f"/><rect x="6" y="1" width="3" height="6" fill="#7cbc5f"/><rect x="17" y="1" width="3" height="6" fill="#7cbc5f"/><g fill="#fff"><rect x="5" y="11" width="4" height="3"/><rect x="11" y="11" width="4" height="3"/><rect x="17" y="11" width="4" height="3"/><rect x="5" y="17" width="4" height="3"/><rect x="11" y="17" width="4" height="3"/><rect x="17" y="17" width="4" height="3"/></g></svg>February 04,2023</div>
  <h4>Lorem ipsum dolor sit amet, conse ctetur magna dolor aliqua.</h4>
  <p>Lorem ipsum dolor sit amet, consectetur adipiscing elit, sed do eiusmod tempor incididunt ut labore et &nbsp;magna aliqua.</p>
  <a class="more" href="#">READ MORE</a>
</article>

<footer class="abs contact">
  <div class="contact-photo" role="img" aria-label="Dark photo of a road crew working beside traffic cones"></div>
  <svg class="contact-curve" width="1200" height="200" viewBox="0 0 1200 200">
    <path d="M0 0 L1200 0 L1200 170 C900 20 350 20 0 190Z" fill="#fff"/>
    <path d="M0 178 C350 8 900 8 1200 158" fill="none" stroke="#e8913f" stroke-width="12"/>
  </svg>
  <h2>Contact Us</h2>
  <div class="field" style="left:258px;top:242px;width:217px;height:36px">Name</div>
  <div class="field" style="left:489px;top:242px;width:217px;height:36px">Email Address</div>
  <div class="field" style="left:720px;top:242px;width:218px;height:36px">Phone Number</div>
  <div class="field" style="left:258px;top:310px;width:684px;height:115px">Message</div>
  <a class="btn" href="#">SUBMIT</a>
  <div class="rule"></div>
  <nav class="footer-nav"><a href="#">Home</a><a href="#">About Us</a><a href="#">Services</a><a href="#">Traffic Cones</a><a href="#">Contact us</a></nav>
  <p class="copyright">Copyrights ©2023 Bluefern Safety Products. All Rights Reserved</p>
  <div class="footer-mail"><span class="mail-dot"><svg width="14" height="10" viewBox="0 0 14 10"><rect x="0.5" y="0.5" width="13" height="9" rx="1" fill="none" stroke="#fff"/><path d="M1 1l6 5 6-5" fill="none" stroke="#fff"/></svg></span>info@bluefernworks.com</div>
</footer>

</body>
</html>
```